Corvallin Property Solutions need a business card design

Hello guys. We would need a business card design asap please.
We are a start up property investment business based in London UK specialised in buying, selling, managing and letting properties and helping distressed property owners.
The name of our Business is Corvallin, the logo symbolises the four fundamental elements of the world (earth, air, fire and water) and so it stands for strength, stability, longevity.
We would like the business card to communicate professionalism and reliability. Many many thanks indeed for your work.

Details:

1.) Marisol Dunkley
Property Investor
Mobile: +44(0)7700362517
Email: marisol.corvallin@quilbrook.example

2.) Tomas Brindle
Property Investor
Mobile: +44(0)7700845926
Email: tomas.corvallin@quilbrook.example

Industry/Entity Type

Investment

```html
<!DOCTYPE html>
<html lang="en">
<head>
<meta charset="utf-8">
<title>Corvallin Property Solutions – Business Cards</title>
<link rel="stylesheet" href="https://fonts.googleapis.com/css2?family=Exo+2:ital,wght@0,500;0,700;0,800;1,700&family=Arimo:wght@400;700&display=swap">
<style>
  :root {
    --backdrop: #e9e4dc;
    --card-white: #ffffff;
    --band-blue: #3342b4;
    --name-blue: #1f2f9a;
    --ink-dark: #1a1a2a;
    --brand-ink: #141414;
    --text-light: #ffffff;
    --dot-red: #d8352f;
  }
  * { margin: 0; padding: 0; box-sizing: border-box; }
  html, body {
    width: 1200px;
    height: 778px;
    overflow: hidden;
    background: var(--backdrop);
  }
  .canvas {
    position: relative;
    width: 1200px;
    height: 778px;
  }
  .business-card {
    position: absolute;
    width: 520px;
    height: 320px;
    background: var(--card-white);
    border-radius: 18px;
    overflow: hidden;
    box-shadow: 0 4px 14px rgba(0, 0, 0, 0.18);
  }
  .card-tomas { left: 60px; top: 70px; }
  .card-marisol { left: 620px; top: 388px; }

  .identity {
    position: absolute;
    left: 0;
    top: 0;
    width: 100%;
    height: 222px;
    display: flex;
    flex-direction: column;
    align-items: center;
    justify-content: center;
    text-align: center;
    padding-top: 18px;
  }
  .brand {
    display: flex;
    align-items: center;
    gap: 8px;
    font-family: "Exo 2", sans-serif;
    font-weight: 800;
    font-size: 24px;
    letter-spacing: 1px;
    color: var(--brand-ink);
    text-transform: uppercase;
  }
  .brand-dot {
    width: 12px;
    height: 12px;
    border-radius: 50%;
    background: var(--dot-red);
  }
  .brand-tagline {
    margin-top: 2px;
    font-family: "Arimo", sans-serif;
    font-weight: 700;
    font-size: 9px;
    letter-spacing: 1.5px;
    color: var(--brand-ink);
    text-transform: uppercase;
  }
  .person-name {
    margin-top: 22px;
    font-family: "Exo 2", sans-serif;
    font-weight: 700;
    font-style: italic;
    font-size: 28px;
    letter-spacing: 0.5px;
    color: var(--name-blue);
    text-transform: uppercase;
  }
  .person-role {
    margin-top: 4px;
    font-family: "Arimo", sans-serif;
    font-weight: 700;
    font-size: 13px;
    letter-spacing: 0.5px;
    color: var(--ink-dark);
    text-transform: uppercase;
  }

  .contact-band {
    position: absolute;
    left: 0;
    bottom: 0;
    width: 100%;
    height: 98px;
    background: var(--band-blue);
    color: var(--text-light);
    padding: 20px 0 0 44px;
  }
  .contact-mobile {
    font-family: "Exo 2", sans-serif;
    font-weight: 500;
    font-size: 24px;
    letter-spacing: 2.5px;
  }
  .contact-email {
    margin-top: 6px;
    padding-left: 16px;
    font-family: "Arimo", sans-serif;
    font-size: 17px;
  }
</style>
</head>
<body>
<main class="canvas">

  <section class="business-card card-tomas">
    <div class="identity">
      <div class="brand"><span class="brand-dot"></span>Corvallin</div>
      <div class="brand-tagline">Property Solutions</div>
      <h1 class="person-name">Tomas Brindle</h1>
      <p class="person-role">Property Investor</p>
    </div>
    <div class="contact-band">
      <p class="contact-mobile">Mobile: +44(0) 7700845926</p>
      <p class="contact-email">E.mail: tomas.corvallin@quilbrook.example</p>
    </div>
  </section>

  <section class="business-card card-marisol">
    <div class="identity">
      <div class="brand"><span class="brand-dot"></span>Corvallin</div>
      <div class="brand-tagline">Property Solutions</div>
      <h1 class="person-name">Marisol Dunkley</h1>
      <p class="person-role">Property Investor</p>
    </div>
    <div class="contact-band">
      <p class="contact-mobile">Mobile: +44(0) 7700362517</p>
      <p class="contact-email">E.mail: marisol.corvallin@quilbrook.example</p>
    </div>
  </section>

</main>
</body>
</html>
```